Crestmoor Business Cards

I need a business card designed with the following information.

Company Name: Crestmoor Wealth Management
Name: BriAnne Tolvey
Title: Executive Assistant
Cell: (555) 302-7164
Direct Line: (555) 917-5082
Email: brianne@crestmoorwm.example
Address: 20537 W. Harwell PKWY Ste. B
Fernridge, TX 77512

I have attached the logo.
I would like it in navy blue and silver.
Thanks.

```html
<!DOCTYPE html>
<html lang="en">
<head>
<meta charset="utf-8">
<title>Crestmoor Wealth Management – Business Card</title>
<link rel="stylesheet" href="https://fonts.googleapis.com/css2?family=Source+Sans+3:wght@400;600&family=Questrial&display=swap">
<style>
  :root {
    --navy: #13243f;
    --silver-line: #a9aaac;
    --stage: #d3d4d6;
    --card-white: #ffffff;
    --card-grey: #747474;
    --ink-grey: #6b6b6b;
    --ink-dark: #1c1c1c;
  }
  * { box-sizing: border-box; margin: 0; padding: 0; }
  html, body { width: 1200px; height: 1107px; overflow: hidden; }
  body {
    background: var(--stage);
    font-family: "Source Sans 3", Arial, sans-serif;
    position: relative;
  }
  .card {
    position: absolute;
    width: 840px;
    height: 460px;
    border-radius: 26px;
    overflow: hidden;
  }
  .card-back {
    left: 290px;
    top: 560px;
    background: var(--card-grey);
    color: #fff;
    z-index: 1;
  }
  .back-mark {
    position: absolute;
    left: 0; right: 0; top: 110px;
    display: flex; flex-direction: column; align-items: center; gap: 20px;
  }
  .back-mark .mark-square { width: 60px; height: 60px; background: #fff; }
  .back-mark .mark-name {
    font-size: 40px; font-weight: 400; letter-spacing: 8px; text-transform: uppercase;
  }
  .back-mark .mark-sub {
    font-size: 17px; font-weight: 400; letter-spacing: 5px; text-transform: uppercase;
  }
  .website {
    position: absolute; left: 0; right: 0; top: 372px;
    text-align: center; font-size: 26px; letter-spacing: 3.5px;
  }
  .card-front {
    left: 110px;
    top: 110px;
    background: var(--card-white);
    border: 1px solid #8e8e8e;
    z-index: 2;
  }
  .brand {
    position: absolute; left: 60px; top: 80px; width: 340px;
    display: flex; flex-direction: column; align-items: center;
    color: var(--navy);
  }
  .brand .mark-square { width: 70px; height: 70px; background: var(--navy); margin-bottom: 36px; }
  .brand .mark-name {
    font-size: 40px; font-weight: 400; letter-spacing: 12px; text-transform: uppercase;
  }
  .brand .mark-sub {
    font-size: 15px; font-weight: 400; letter-spacing: 4.5px; text-transform: uppercase; margin-top: 6px;
  }
  .divider {
    position: absolute; left: 430px; top: 85px; width: 2px; height: 190px;
    background: var(--silver-line);
  }
  .contact { position: absolute; left: 462px; top: 80px; }
  .person-name {
    font-family: "Questrial", Arial, sans-serif;
    font-size: 28px; font-weight: 400; color: var(--navy);
  }
  .person-title {
    font-family: "Questrial", Arial, sans-serif;
    font-size: 22px; font-weight: 400; color: var(--ink-grey); margin-top: 2px; letter-spacing: 0.5px;
  }
  .contact-list { list-style: none; margin-top: 30px; }
  .contact-list li {
    display: flex; align-items: center; gap: 8px;
    font-size: 20px; color: var(--ink-dark); line-height: 1.6;
  }
  .contact-list svg { width: 20px; height: 20px; flex: none; }
  .address-band {
    position: absolute; left: 0; right: 0; top: 350px;
  }
  .address-band .rule { height: 2px; background: var(--silver-line); }
  .address-band .band {
    height: 48px; margin: 5px 0;
    background: var(--navy); color: #fff;
    display: flex; align-items: center; justify-content: center;
    font-size: 20px;
  }
</style>
</head>
<body>

  <section class="card card-back" aria-label="Business card back">
    <div class="back-mark">
      <div class="mark-square"></div>
      <div class="mark-name">Crestmoor</div>
      <div class="mark-sub">Wealth Management</div>
    </div>
    <p class="website">www.crestmoorwm.example</p>
  </section>

  <section class="card card-front" aria-label="Business card front">
    <div class="brand">
      <div class="mark-square"></div>
      <div class="mark-name">Crestmoor</div>
      <div class="mark-sub">Wealth Management</div>
    </div>

    <div class="divider"></div>

    <div class="contact">
      <h1 class="person-name">BriAnne Tolvey</h1>
      <p class="person-title">Executive Assistant</p>
      <ul class="contact-list">
        <li>
          <svg viewBox="0 0 20 20" aria-hidden="true"><circle cx="10" cy="10" r="8.6" fill="none" stroke="#13243f" stroke-width="1.6"/><path d="M6.6 5.6c.5-.4 1.1-.3 1.4.2l.9 1.5c.3.5.2 1-.2 1.3l-.6.5c.5 1.1 1.4 2 2.5 2.5l.5-.6c.3-.4.9-.5 1.3-.2l1.5.9c.5.3.6.9.2 1.4-.7.9-1.7 1.2-2.7.8-2.4-.9-4.3-2.8-5.2-5.2-.4-1 0-2.1.7-2.8z" fill="#13243f"/></svg>
          (555) 302-7164
        </li>
        <li>
          <svg viewBox="0 0 20 20" aria-hidden="true"><circle cx="10" cy="10" r="8.6" fill="none" stroke="#13243f" stroke-width="1.6"/><path d="M6.6 5.6c.5-.4 1.1-.3 1.4.2l.9 1.5c.3.5.2 1-.2 1.3l-.6.5c.5 1.1 1.4 2 2.5 2.5l.5-.6c.3-.4.9-.5 1.3-.2l1.5.9c.5.3.6.9.2 1.4-.7.9-1.7 1.2-2.7.8-2.4-.9-4.3-2.8-5.2-5.2-.4-1 0-2.1.7-2.8z" fill="#13243f"/></svg>
          (555) 917-5082(Direct Line)
        </li>
        <li>
          <svg viewBox="0 0 20 20" aria-hidden="true"><circle cx="10" cy="10" r="8.6" fill="none" stroke="#13243f" stroke-width="1.6"/><rect x="5.5" y="7" width="9" height="6.5" rx="0.8" fill="#13243f"/><path d="M5.8 7.4 10 10.6l4.2-3.2" fill="none" stroke="#fff" stroke-width="1"/></svg>
          brianne@crestmoorwm.example
        </li>
      </ul>
    </div>

    <div class="address-band">
      <div class="rule"></div>
      <div class="band">20537 W. Harwell PKWY Ste. B, Fernridge, TX 77512</div>
      <div class="rule"></div>
    </div>
  </section>

</body>
</html>
```